*** Business Card Design Project

I need a logo and business card for my new catering business: "Brevano". The design should be modern, clean, elegant and refined. One or Two colours only. The design SHOULD NOT include graphics or images. There should be space for my name, phone number and email address (I will provide these to you later).

Industry/Entity Type

Catering

Requirements
Must have
• Must have one or two colours only.
Must include the text "brevano"
Should not have
• Must not have graphics or images.

```html
<!DOCTYPE html>
<html lang="en">
<head>
<meta charset="utf-8">
<title>Brevano – Business Card</title>
<link rel="stylesheet" href="https://fonts.googleapis.com/css2?family=Cinzel:wght@400&family=Arimo:wght@400;700&display=swap">
<style>
  :root {
    --bg-top: #4a4a4a;
    --bg-bottom: #0b0b0b;
    --ink: #3c3c3c;
    --text: #111111;
    --paper: #f6f6f6;
    --paper-edge: #e2e2e2;
    --gold-light: #ffd66b;
    --gold-mid: #f0ae2c;
    --gold-deep: #c98a12;
    --white: #ffffff;
  }
  * { margin: 0; padding: 0; box-sizing: border-box; }
  html, body { width: 1192px; height: 1200px; overflow: hidden; }
  body {
    background: radial-gradient(ellipse at 50% 20%, var(--bg-top) 0%, #262626 55%, var(--bg-bottom) 100%);
    font-family: "Arimo", Arial, sans-serif;
    position: relative;
  }
  .wordmark {
    font-family: "Cinzel", "Times New Roman", serif;
    font-weight: 400;
    letter-spacing: 1px;
    line-height: 1;
    white-space: nowrap;
  }
  .hero-mark {
    position: absolute;
    top: 120px;
    left: 0;
    width: 100%;
    text-align: center;
    font-size: 92px;
    color: var(--white);
  }
  .card {
    position: absolute;
    left: 256px;
    width: 680px;
    height: 390px;
    border-radius: 3px;
    box-shadow: 0 18px 40px rgba(0,0,0,0.55);
  }
  .card-front {
    top: 270px;
    background: linear-gradient(160deg, var(--white) 0%, var(--paper) 70%, var(--paper-edge) 100%);
    color: var(--text);
  }
  .card-front .wordmark {
    position: absolute;
    top: 52px;
    left: 50px;
    font-size: 68px;
    color: var(--ink);
  }
  .holder {
    position: absolute;
    left: 50px;
    top: 232px;
    font-size: 17px;
    line-height: 1.25;
  }
  .holder-name { font-weight: 700; }
  .contact {
    position: absolute;
    left: 420px;
    top: 176px;
    font-size: 16px;
    line-height: 1.25;
  }
  .address { margin-bottom: 22px; }
  .contact-list { list-style: none; }
  .contact-list li { display: flex; align-items: center; gap: 8px; }
  .contact-list svg { width: 13px; height: 13px; flex: none; }
  .website { margin-top: 12px; }
  .card-back {
    top: 720px;
    background:
      radial-gradient(ellipse at 22% 18%, rgba(255,240,180,0.9) 0%, rgba(255,240,180,0) 45%),
      radial-gradient(ellipse at 80% 85%, rgba(255,214,110,0.8) 0%, rgba(255,214,110,0) 50%),
      linear-gradient(135deg, var(--gold-light) 0%, var(--gold-mid) 40%, var(--gold-deep) 65%, var(--gold-mid) 100%);
    display: flex;
    align-items: center;
    justify-content: center;
  }
  .card-back .wordmark {
    font-size: 84px;
    color: var(--white);
  }
</style>
</head>
<body>
  <div class="wordmark hero-mark">Brevano</div>

  <section class="card card-front">
    <div class="wordmark">Brevano</div>
    <div class="holder">
      <div class="holder-name">Elena Ross</div>
      <div class="holder-title">Managing Director</div>
    </div>
    <div class="contact">
      <div class="address">P.O Box 000<br>Your city, Zip 0000</div>
      <ul class="contact-list">
        <li>
          <svg viewBox="0 0 14 14" aria-hidden="true"><circle cx="7" cy="7" r="6.2" fill="none" stroke="#111" stroke-width="1.2"/><path d="M4.5 4.2c.4-.4.9-.3 1.1.1l.5.9c.2.3.1.6-.2.8l-.3.2c.3.8.9 1.4 1.7 1.7l.2-.3c.2-.3.5-.4.8-.2l.9.5c.4.2.5.7.1 1.1-.5.5-1.2.7-2 .3-1.5-.7-2.7-1.9-3.3-3.3-.2-.7 0-1.4.5-1.8z" fill="#111"/></svg>
          <span>00000 00000</span>
        </li>
        <li>
          <svg viewBox="0 0 14 14" aria-hidden="true"><circle cx="7" cy="7" r="6.2" fill="none" stroke="#111" stroke-width="1.2"/><rect x="5" y="3.3" width="4" height="7.4" rx=".8" fill="#111"/><rect x="5.7" y="4.2" width="2.6" height="4.6" fill="#fff"/></svg>
          <span>00000 00000</span>
        </li>
        <li>
          <svg viewBox="0 0 14 14" aria-hidden="true"><circle cx="7" cy="7" r="6.2" fill="none" stroke="#111" stroke-width="1.2"/><rect x="3.8" y="6" width="6.4" height="3.6" rx=".5" fill="#111"/><rect x="5" y="3.8" width="4" height="2.4" fill="#111"/></svg>
          <span>00000 00000</span>
        </li>
        <li>
          <svg viewBox="0 0 14 14" aria-hidden="true"><circle cx="7" cy="7" r="6.2" fill="#111"/><rect x="3.8" y="4.8" width="6.4" height="4.4" fill="#fff"/><path d="M3.8 4.8 7 7.4l3.2-2.6" fill="none" stroke="#111" stroke-width=".8"/></svg>
          <span>elena@yourdomain.com</span>
        </li>
      </ul>
      <div class="website">www.yourdomain.com</div>
    </div>
  </section>

  <section class="card card-back">
    <div class="wordmark">Brevano</div>
  </section>
</body>
</html>
```